依頼概要
■依頼の目的/概要
小学生バレーボールのスポーツ少年団でメンバーを募集するためのポスターの作成をお願いします。

■依頼詳細
ポスターは男子チーム、女子チーム兼用となります。主に教室での直接配布、校内の掲示板や近隣の施設(コンビニや公民館等)での掲示を目的としたものになります。

必要に応じて写真の背景等を加工いただいても構いません。

楽しそうなイメージだけでなく、スポーツに関心のある子どもたちがバレーボールを“かっこいい”と感じてくれるような躍動感の伝わるものを希望しています。

■重視する点
・明るくインパクトのあるデザイン
・できるだけ躍動感の伝わるもの
・読みやすい文字であること

■サイズ
A4サイズでお願いします。
メインはA4ですが、B4(A4の122%)にも対応する画素数でお願いいたします

■その他
・レイアウトイメージ、素材は添付ファイルにてご確認ください
・写真やイラストの素材は当方で用意していますが、用意したもの以外の素材を使っていただいても構いません。
・レイアウトのイメージやキャッチコピー、掲載する文言等は添付の「レイアウトイメージ.pdf」「レイアウト説明.txt」を参照ください。レイアウトは当方のイメージと異なるものになっても構いません。

何かご不明な点がございましたら、お気軽にご質問下さい。
どうぞよろしくお願いいたします。
納品いただくデータですが、納品後に当方で編集することがあるため、フォトショップまたはイラストレーターで編集できるかたちで納品いただけますと幸いです。よろしくお願いします。

```html
<!DOCTYPE html>
<html lang="ja">
<head>
<meta charset="utf-8">
<title>若葉バレースポーツ少年団 メンバー募集</title>
<link href="https://fonts.googleapis.com/css2?family=Dela+Gothic+One&family=M+PLUS+Rounded+1c:wght@500;700;800&family=Noto+Sans+JP:wght@500;700;900&display=swap" rel="stylesheet">
<style>
  :root {
    --red: #e0141e;
    --deep-red: #b80d15;
    --ink: #222222;
    --paper: #ffffff;
    --photo-a: #c9b89a;
    --photo-b: #8f7f6a;
    --kid-a: #f4c9a8;
    --kid-b: #d9343a;
  }
  * { margin: 0; padding: 0; box-sizing: border-box; }
  html, body { width: 849px; height: 1200px; overflow: hidden; background: var(--paper); }
  body { font-family: "Noto Sans JP", sans-serif; color: var(--ink); }
  .poster { position: relative; width: 849px; height: 1200px; background: var(--paper); overflow: hidden; }

  .illust { position: absolute; border-radius: 50%; background: radial-gradient(circle at 50% 40%, var(--kid-a), var(--kid-b)); }
  .illust--top-left { left: 18px; top: 14px; width: 104px; height: 120px; }
  .illust--top-right { right: 18px; top: 8px; width: 110px; height: 128px; }
  .illust--ball-left { left: 140px; top: 96px; width: 32px; height: 32px; background: radial-gradient(circle, #fff, #f2c230); }
  .illust--ball-right { right: 140px; top: 100px; width: 30px; height: 30px; background: radial-gradient(circle, #fff, #2f6fd1); }
  .illust--mid-left { left: 20px; top: 905px; width: 96px; height: 112px; }
  .illust--mid-right { right: 8px; top: 900px; width: 78px; height: 110px; }
  .illust--bottom-left { left: 6px; top: 1112px; width: 66px; height: 76px; }

  .headline { position: absolute; left: 0; right: 0; top: 6px; height: 228px; text-align: center; font-family: "M PLUS Rounded 1c", sans-serif; }
  .headline__lead { display: block; height: 66px; font-size: 56px; line-height: 66px; font-weight: 800; letter-spacing: 4px; margin-left: 110px; }
  .headline__main { display: block; height: 100px; font-family: "Dela Gothic One", sans-serif; font-size: 92px; line-height: 100px; color: var(--red); letter-spacing: 2px; transform: rotate(-3deg); margin-left: -60px; -webkit-text-stroke: 3px var(--ink); paint-order: stroke fill; }
  .headline__tail { display: block; height: 60px; font-size: 52px; line-height: 60px; font-weight: 800; letter-spacing: 4px; margin-left: 330px; }

  .collage { position: absolute; left: 28px; top: 244px; width: 793px; height: 426px; border-radius: 6px; background: linear-gradient(135deg, var(--photo-a), var(--photo-b) 55%, #6c5d4c); }

  .banner { position: absolute; left: 0; top: 680px; width: 849px; height: 104px; background: var(--red); border-top: 4px solid var(--deep-red); border-bottom: 4px solid var(--deep-red); text-align: center; color: var(--paper); font-weight: 900; padding-top: 4px; }
  .banner__team { display: block; font-size: 38px; letter-spacing: 2px; line-height: 46px; }
  .banner__call { display: block; font-size: 42px; letter-spacing: 3px; line-height: 48px; }

  .practice { position: absolute; left: 60px; top: 808px; font-weight: 700; }
  .practice__title { font-size: 22px; font-weight: 900; margin-bottom: 4px; }
  .practice__row { display: flex; font-size: 18px; line-height: 1.5; }
  .practice__day { width: 110px; }
  .practice__time { width: 84px; }

  .message { position: absolute; left: 132px; top: 935px; width: 620px; font-size: 19px; font-weight: 700; line-height: 1.6; }

  .divider { position: absolute; left: 30px; right: 30px; top: 1030px; height: 4px; background: var(--red); }

  .info-left { position: absolute; left: 80px; top: 1050px; font-size: 17px; font-weight: 700; line-height: 1.6; }
  .info-left__items { margin-top: 16px; }
  .info-right { position: absolute; left: 470px; top: 1050px; font-weight: 700; }
  .info-right__lead { font-size: 17px; }
  .info-right__phone { display: flex; align-items: center; gap: 8px; font-size: 32px; font-weight: 900; color: var(--red); margin: 6px 0; white-space: nowrap; }
  .info-right__phone svg { width: 28px; height: 28px; }
  .info-right__person { font-size: 15px; }
</style>
</head>
<body>
<main class="poster">
  <div class="illust illust--top-left" role="img" aria-label="バレーボールをするこどものイラスト"></div>
  <div class="illust illust--ball-left" role="img" aria-label="バレーボールのイラスト"></div>
  <div class="illust illust--top-right" role="img" aria-label="スパイクするこどものイラスト"></div>
  <div class="illust illust--ball-right" role="img" aria-label="バレーボールのイラスト"></div>

  <h1 class="headline">
    <span class="headline__lead">そうだ、</span>
    <span class="headline__main">バレーボール</span>
    <span class="headline__tail">しよう。</span>
  </h1>

  <div class="collage" role="img" aria-label="練習風景や試合、集合写真のコラージュと手書きのコメント"></div>

  <section class="banner">
    <span class="banner__team">若葉バレースポーツ少年団</span>
    <span class="banner__call">男女新メンバー募集!!</span>
  </section>

  <section class="practice">
    <p class="practice__title">■ 練習日(毎週)</p>
    <p class="practice__row"><span class="practice__day">土・日曜日</span><span class="practice__time">9:00~</span><span>若葉小学校体育館・若葉西小学校体育館</span></p>
    <p class="practice__row"><span class="practice__day">水曜日</span><span class="practice__time">17:30~</span><span>若葉小学校体育館</span></p>
  </section>

  <div class="illust illust--mid-left" role="img" aria-label="レシーブするこどものイラスト"></div>
  <p class="message">みんなが下の名まえでよびあう若葉バレーは仲のよさがじまん!<br>いろいろな小学校から集まっているから友達もたくさんできるよ!</p>
  <div class="illust illust--mid-right" role="img" aria-label="ボールを持つこどものイラスト"></div>

  <div class="divider"></div>

  <section class="info-left">
    <p>見学・体験はいつでも受け付けています!<br>連絡は右記の担当 森川まで。</p>
    <p class="info-left__items">持ち物:上ぐつ、水とう、動きやすい服そう</p>
  </section>

  <section class="info-right">
    <p class="info-right__lead">詳しくはお問合せください</p>
    <p class="info-right__phone">
      <svg viewBox="0 0 24 24" aria-hidden="true"><path fill="currentColor" d="M6.6 10.8a15.1 15.1 0 0 0 6.6 6.6l2.2-2.2a1 1 0 0 1 1-.25 11.4 11.4 0 0 0 3.6.57 1 1 0 0 1 1 1V20a1 1 0 0 1-1 1A17 17 0 0 1 3 4a1 1 0 0 1 1-1h3.5a1 1 0 0 1 1 1c0 1.25.2 2.45.57 3.57a1 1 0 0 1-.25 1z"/></svg>
      090-XXXX-XXXX
    </p>
    <p class="info-right__person">育成会会長 森川(もりかわ)</p>
  </section>

  <div class="illust illust--bottom-left" role="img" aria-label="こどものイラスト"></div>
</main>
</body>
</html>
```